Business Card Design Project

I need a new business card design for my building/development company: Kestrel Ridge Builders.

We specialise in small sub-divisions, multi-story developments and new house builds.
We handle the whole process from concept stage right throught to a fully developed property.
Updates

Target Market(s)

people looking to develop their property and need help. New property buyers

Industry/Entity Type

House

Requirements
Must have
• My logo on both sides:
Side 1: Logo taking up whole side as per old card but with a color/style change.

Side 2: Contact page: include logo but the rest just surprise me!

All contact details will be: (and need to be changable for each employee) I'll inform you of specifics before printing.

Name Surname
Position ie. Managing director
M: insert mobile
E: insert email
P.O. Box 518, Ashwell, Vic, 3094
www.kestrelridgebuilders.com.au

Nice to have
• Colors i'd like: (not necessarily all but this is the basic idea)

Black, blue, grey, silver, white

```html
<!DOCTYPE html>
<html lang="en">
<head>
<meta charset="utf-8">
<title>Kestrel Ridge Builders – Stationery</title>
<link rel="stylesheet" href="https://fonts.googleapis.com/css2?family=Arimo:wght@400&family=Tinos:wght@400&display=swap">
<style>
  :root{
    --page:#eef0f3;
    --blue-deep:#0a3f8c;
    --blue-mid:#1a63c0;
    --blue-light:#2f80dd;
    --white:#ffffff;
    --silver:#e6e8eb;
    --ink:#3a3a3a;
    --brand:#1d6fcf;
  }
  *{margin:0;padding:0;box-sizing:border-box}
  html,body{width:1200px;height:795px;overflow:hidden;background:var(--page)}
  .canvas{position:relative;width:1200px;height:795px}

  .card{position:absolute;width:535px;height:362px;border-radius:16px;overflow:hidden;
    box-shadow:0 4px 10px rgba(0,0,0,.35)}
  .card--front{left:44px;top:57px;
    background:radial-gradient(ellipse at 45% 40%,var(--blue-light) 0%,var(--blue-mid) 35%,var(--blue-deep) 100%)}
  .card--back{left:617px;top:57px;
    background:radial-gradient(ellipse at 40% 70%,var(--blue-light) 0%,var(--blue-mid) 40%,var(--blue-deep) 100%)}

  .brand{position:absolute;display:flex;align-items:center;gap:10px;
    font-family:"Arimo",Arial,sans-serif;font-weight:400;color:var(--brand);white-space:nowrap;line-height:1}
  .brand__mark{background:var(--brand);flex:none}
  .card--front .brand{left:0;right:0;top:160px;justify-content:center;font-size:38px;color:var(--white)}
  .card--front .brand__mark{width:38px;height:38px;background:var(--white)}

  .back-panel{position:absolute;left:0;top:0;width:535px;height:362px}
  .card--back .brand{left:22px;top:98px;font-size:21px}
  .card--back .brand__mark{width:22px;height:22px}

  .contact{position:absolute;font-family:"Tinos","Times New Roman",serif;color:var(--white)}
  .contact__name{right:22px;top:10px;font-size:28px;text-align:right}
  .contact__role{right:22px;top:46px;font-size:18px;text-align:right}
  .contact__details{right:22px;top:196px;font-size:20px;line-height:1.32;text-align:right}
  .contact__web{left:22px;top:322px;font-size:18px}

  .envelope{position:absolute;left:115px;top:500px;width:540px;height:245px;
    background:radial-gradient(ellipse at 40% 30%,var(--white) 0%,var(--silver) 100%);
    box-shadow:0 4px 12px rgba(0,0,0,.3)}
  .envelope__rule{position:absolute;left:0;right:0;top:8px;height:4px;background:var(--blue-mid)}
  .envelope .brand{right:22px;top:168px;font-size:20px}
  .envelope .brand__mark{width:20px;height:20px}
  .envelope__address{position:absolute;right:22px;top:205px;
    font-family:"Arimo",Arial,sans-serif;font-size:13px;color:var(--ink)}
</style>
</head>
<body>
<main class="canvas">

  <section class="card card--front" aria-label="Business card front">
    <div class="brand"><span class="brand__mark"></span>Kestrel Ridge Builders</div>
  </section>

  <section class="card card--back" aria-label="Business card back">
    <svg class="back-panel" viewBox="0 0 535 362" aria-hidden="true">
      <defs>
        <linearGradient id="panelFill" x1="0" y1="0" x2="1" y2="1">
          <stop offset="0" stop-color="#ffffff"/>
          <stop offset="1" stop-color="#e9ecf0"/>
        </linearGradient>
      </defs>
      <polygon points="0,0 264,0 396,108 0,238" fill="#7fb3ea" opacity=".7"/>
      <polygon points="0,0 250,0 380,108 0,230" fill="url(#panelFill)"/>
    </svg>
    <div class="brand"><span class="brand__mark"></span>Kestrel Ridge Builders</div>
    <p class="contact contact__name">Name Surname</p>
    <p class="contact contact__role">Managing director</p>
    <p class="contact contact__details">M: insert mobile<br>E: insert email<br>P.O. Box 518, Ashwell, Vic, 3094</p>
    <p class="contact contact__web">www.kestrelridgebuilders.com.au</p>
  </section>

  <section class="envelope" aria-label="Envelope">
    <div class="envelope__rule"></div>
    <div class="brand"><span class="brand__mark"></span>Kestrel Ridge Builders</div>
    <p class="envelope__address">P.O. Box 518, Ashwell, Vic, 3094</p>
  </section>

</main>
</body>
</html>
```